Commercial Real Estate website

Need a web design commercial real estate company specializing in retail shopping centers based in Orlando, FL. We would like pictures of Orlando city skyline with hues and colors that go with hot pink. We want to stress the relationship of time on the value of real estate.
It should gave a rotating page that highlights our property listings.

Target Market(s)

Owners of shopping centers and national retail tenants looking for tenant representatives.

Industry/Entity Type

Real Estate

Number of Pages Required

5+ page

Font styles to use
Serif

Colors
e34197

Requirements
Must have
• Pictures of commercial retail grocery anchored shopping centers and city scapes and skylines.

```html
<!DOCTYPE html>
<html lang="en">
<head>
<meta charset="utf-8">
<title>Maris Commercial — Making Places Better</title>
<link href="https://fonts.googleapis.com/css2?family=Cinzel:wght@400;700&family=PT+Serif:ital,wght@0,400;0,700;1,400&display=swap" rel="stylesheet">
<style>
:root{
  --pink:#e34197;
  --pink-dark:#c92f80;
  --ink:#2b2b2e;
  --dark:#27272a;
  --grey:#6d6d72;
  --light:#f1f1f3;
  --white:#ffffff;
  --serif:'PT Serif', Georgia, serif;
  --display:'Cinzel', 'Times New Roman', serif;
}
*{box-sizing:border-box;margin:0;padding:0}
html,body{width:1200px;height:3212px;overflow:hidden}
body{font-family:var(--serif);color:var(--ink);background:var(--white);position:relative}
.abs{position:absolute}
section,header,footer{position:absolute;left:0;width:1200px}

/* HERO */
.hero{top:0;height:600px}
.hero-photo{position:absolute;inset:0;background:linear-gradient(180deg,#0d3a7a 0%,#2d7fc7 35%,#6fb4e6 55%,#1b3d66 75%,#0b1b33 100%)}
.topbar{top:0;left:640px;width:500px;height:24px;background:var(--pink);color:#fff;font-size:11px;display:flex;align-items:center;justify-content:center;gap:30px}
.brand{top:22px;left:250px;display:flex;align-items:center;gap:10px;color:#fff}
.brand .mark{width:14px;height:14px;border-radius:50%;background:var(--pink)}
.brand span{font-size:28px;font-weight:700}
.brand small{display:block;font-size:10px;letter-spacing:3px;color:#fff;margin-top:-4px}
.contact{top:34px;left:850px;display:flex;gap:26px;color:#fff;font-size:11px;line-height:1.35}
.contact .item{display:flex;gap:8px;align-items:center}
.contact svg{width:22px;height:22px}
.nav{top:72px;left:330px;width:810px;height:26px;background:var(--pink);display:flex;align-items:center;gap:34px;padding-left:110px;color:#fff;font-size:11px;letter-spacing:1px;text-transform:uppercase}
.headline{top:380px;width:1200px;text-align:center;color:#fff}
.headline h1{font-family:var(--display);font-weight:400;font-size:40px;letter-spacing:3px}
.headline .rule{width:420px;height:1px;background:rgba(255,255,255,.7);margin:6px auto}
.headline .sub{font-family:var(--display);font-size:15px;letter-spacing:3px}
.headline .caption{font-size:13px;margin-top:14px;opacity:.9}
.headline .date{font-family:var(--display);font-size:15px;letter-spacing:2px}

/* ABOUT */
.about{top:540px;height:680px;background:var(--light);clip-path:polygon(0 40px,50% 0,100% 40px,100% 100%,0 100%)}
.about h2{font-family:var(--display);font-size:17px;color:var(--pink);line-height:1.15}
.about h2 em{font-style:normal;color:var(--ink)}
.about p{font-size:11px;line-height:1.6;color:var(--grey)}
.about-copy{top:140px;left:160px;width:250px}
.about-copy .lead{color:var(--pink);margin-top:12px}
.feature-frame{top:90px;left:470px;width:220px;height:210px;border:8px solid var(--pink);border-radius:48px;overflow:hidden;box-shadow:0 6px 16px rgba(0,0,0,.2)}
.feature-frame div{width:100%;height:100%;background:linear-gradient(180deg,#7fb8e8 0%,#bcd8ee 45%,#c9a77a 60%,#8b7358 100%)}
.feature-caption{top:312px;left:470px;width:220px;text-align:center;font-size:10px;color:var(--grey)}
.feature-caption b{display:block;color:var(--pink);font-weight:400}
.expect{top:120px;left:760px;width:270px}
.expect h2{font-size:14px;color:var(--ink)}
.expect .point{margin-top:22px}
.expect h3{font-family:var(--display);font-size:13px;color:var(--pink);display:flex;align-items:center;gap:8px}
.expect h3 i{width:12px;height:12px;border-radius:50%;background:var(--pink);display:inline-block}
.expect p{margin-top:6px}

/* LISTINGS */
.listings{top:1180px;height:640px;background:var(--dark);clip-path:polygon(0 50px,40% 0,100% 30px,100% 100%,0 100%)}
.listings .side{position:absolute;left:0;top:0;width:480px;height:640px;background:linear-gradient(160deg,#ec5aa7,var(--pink) 60%,#d4368a)}
.side .block{position:absolute;left:260px;color:#fff}
.side .big{font-family:var(--display);font-size:30px;line-height:1}
.side .btn{display:inline-block;margin-top:8px;padding:4px 14px;border:1px solid #fff;font-size:9px;letter-spacing:1px}
.side .label{font-family:var(--display);font-size:16px;line-height:1.2}
.cards{position:absolute;left:530px;top:100px;display:grid;grid-template-columns:repeat(3,150px);column-gap:20px;row-gap:38px}
.card{text-align:center;color:#ddd;font-size:9px;line-height:1.5}
.card .thumb{width:120px;height:120px;margin:0 auto 8px;border:5px solid var(--pink);border-radius:24px;background:linear-gradient(180deg,#79b4e6 0%,#b8d6ee 45%,#c39e6c 62%,#7d6246 100%)}
.card h4{color:var(--pink);font-weight:400;font-size:10px}
.card .go{margin-top:6px;background:var(--pink);color:#fff;padding:3px 0;font-size:8px;letter-spacing:1px}

/* NEWS */
.news{top:1800px;height:380px}
.news-photo{position:absolute;inset:0;background:linear-gradient(90deg,#b9a79a 0%,#e6d8cc 40%,#f1e8df 60%,#bfae9f 100%)}
.news-box{top:70px;left:250px;width:700px;height:190px;background:var(--pink);color:#fff;text-align:center;padding:22px 70px}
.news-box h2{font-size:20px;font-weight:400}
.news-box .quote{font-size:28px;line-height:1;margin-top:8px}
.news-box p{font-size:11px;line-height:1.6}
.news-box .btn{display:inline-block;margin-top:14px;border:1px solid #fff;padding:4px 16px;font-size:9px;letter-spacing:1px}

/* GALLERY */
.gallery{top:2170px;height:630px}
.gallery-photo{position:absolute;inset:0;background:linear-gradient(180deg,#d8d8da 0%,#a9a9ad 50%,#8c8c90 100%)}
.gallery h2{position:absolute;top:90px;width:1200px;text-align:center;font-family:var(--display);font-size:18px;color:var(--ink)}
.arrow{top:84px;width:26px;height:26px;background:var(--pink);display:flex;align-items:center;justify-content:center}
.arrow svg{width:12px;height:12px}
.shots{position:absolute;left:270px;top:150px;display:grid;grid-template-columns:repeat(3,200px);column-gap:30px;row-gap:44px}
.shot{height:130px;border-radius:10px;border:4px solid #fff;box-shadow:0 4px 12px rgba(0,0,0,.3)}
.s1{background:linear-gradient(180deg,#7fa9d6,#c1543a 60%,#6d3b2c)}
.s2{background:linear-gradient(180deg,#6d97c8,#9b8c7b 55%,#4d4138)}
.s3{background:linear-gradient(180deg,#8fb9e2,#d5b78f 60%,#8a6a4c)}
.s4{background:linear-gradient(180deg,#4a3020,#b5865a 55%,#3a2818)}
.s5{background:linear-gradient(180deg,#d88a5c,#7b6a8c 55%,#2f2a36)}
.s6{background:linear-gradient(180deg,#e0dcd2,#b7a68d 55%,#6f6352)}

/* FOOTER */
.footer{top:2790px;height:422px;background:linear-gradient(180deg,#2a2a2e,#1c1c20);color:#bbb;clip-path:polygon(0 20px,50% 0,100% 20px,100% 100%,0 100%)}
.footer .cta{position:absolute;top:60px;width:1200px;text-align:center;color:#fff}
.cta h2{font-family:var(--display);font-size:17px;letter-spacing:1px}
.cta .btn{display:inline-block;margin-top:10px;background:var(--pink);padding:5px 20px;font-size:9px;letter-spacing:1px}
.fcol{top:150px;font-size:10px;line-height:1.7}
.fcol h5{color:var(--pink);font-size:11px;font-weight:400;margin-bottom:6px;text-transform:uppercase;letter-spacing:1px}
.fbrand{display:flex;align-items:center;gap:8px;color:#fff;font-size:22px;font-weight:700;margin-bottom:6px}
.fbrand i{width:12px;height:12px;border-radius:50%;background:var(--pink)}
.social{display:flex;gap:6px}
.social i{width:20px;height:20px;border-radius:50%;background:var(--pink);display:block}
.social i:nth-child(even){background:#4d4d55}
.bottom{top:392px;left:0;width:1200px;height:30px;display:flex;justify-content:space-between;align-items:center;padding:0 140px;font-size:9px;color:#888;border-top:1px solid #3a3a40}
</style>
</head>
<body>

<header class="hero">
  <div class="hero-photo" role="img" aria-label="City skyline at dusk reflected in the lake"></div>
  <div class="abs topbar"><span>Tenant Representation</span><span>Landlord Services</span><span>Investment Sales</span></div>
  <div class="abs brand"><i class="mark"></i><div><span>Maris</span><small>COMMERCIAL</small></div></div>
  <div class="abs contact">
    <div class="item"><svg viewBox="0 0 24 24" fill="none" stroke="#fff" stroke-width="1.6"><rect x="3" y="6" width="18" height="12"/><path d="M3 6l9 7 9-7"/></svg><div>Email Us<br>hello@mariscommercial.com</div></div>
    <div class="item"><div>Contact Us Today<br>(407) 555-0142</div><svg viewBox="0 0 24 24" fill="none" stroke="#fff" stroke-width="1.6"><path d="M6 3h4l2 5-3 2a11 11 0 005 5l2-3 5 2v4a2 2 0 01-2 2A17 17 0 014 5a2 2 0 012-2z"/></svg></div>
  </div>
  <nav class="abs nav"><span>Home</span><span>Our Company</span><span>Featured Listings</span><span>Services</span><span>News</span><span>Contact Us</span></nav>
  <div class="abs headline">
    <h1>· MAKING PLACES · BETTER ·</h1>
    <div class="rule"></div>
    <div class="sub">COMMUNITIES | SHOPPING CENTERS | RETAILERS</div>
    <div class="caption">Orlando City Skyline</div>
    <div class="date">OCTOBER 2013</div>
  </div>
</header>

<section class="about">
  <div class="abs about-copy">
    <h2>ABOUT<br><em>MARIS COMMERCIAL</em></h2>
    <p style="margin-top:14px">Maris Commercial is a full service retail real estate firm based in Orlando, Florida. For more than two decades we have guided owners of grocery anchored shopping centers and national retail tenants through every stage of the property cycle. Our team understands that time shapes value, and we help clients act at the right moment to lease, buy, sell and reposition their centers.</p>
    <p class="lead">From neighborhood centers to regional destinations, we build lasting relationships that make places better for every community we serve.</p>
  </div>
  <div class="abs feature-frame"><div role="img" aria-label="Grocery anchored shopping center storefront"></div></div>
  <div class="abs feature-caption"><b>Briarwood Village</b>Shopping Center</div>
  <div class="abs expect">
    <h2>WHAT YOU CAN EXPECT<br>FROM THE SUMMIT</h2>
    <div class="point"><h3><i></i>COMMUNITIES</h3><p>We study the neighborhoods around each center so tenants and owners meet the real needs of local shoppers.</p></div>
    <div class="point"><h3><i></i>SHOPPING CENTERS</h3><p>Leasing, marketing and sales strategies that protect value and keep anchored centers full over time.</p></div>
    <div class="point"><h3><i></i>RETAILERS</h3><p>Site selection and tenant representation for national brands expanding across Central Florida.</p></div>
  </div>
</section>

<section class="listings">
  <div class="side">
    <div class="block" style="top:150px"><div class="big">FOR<br>LEASE</div><span class="btn">VIEW ALL</span></div>
    <div class="block" style="top:280px"><div class="label">FEATURED<br>LISTINGS</div></div>
    <div class="block" style="top:350px"><div class="big">FOR<br>SALE</div><span class="btn">VIEW ALL</span></div>
  </div>
  <div class="cards">
    <div class="card"><div class="thumb" role="img" aria-label="Shopping center listing"></div><h4>Larkspur Commons</h4>1450 Larkspur Way<br>Orlando, FL 32801<div class="go">VIEW PROPERTY DETAILS</div></div>
    <div class="card"><div class="thumb" role="img" aria-label="Shopping center listing"></div><h4>Fernhollow Plaza</h4>2870 Fernhollow Lane<br>Orlando, FL 32801<div class="go">VIEW PROPERTY DETAILS</div></div>
    <div class="card"><div class="thumb" role="img" aria-label="Shopping center listing"></div><h4>Quillmere Square</h4>615 Quillmere Court<br>Orlando, FL 32801<div class="go">VIEW PROPERTY DETAILS</div></div>
    <div class="card"><div class="thumb" role="img" aria-label="Shopping center listing"></div><h4>Brambleton Crossing</h4>3920 Brambleton Road<br>Orlando, FL 32801<div class="go">VIEW PROPERTY DETAILS</div></div>
    <div class="card"><div class="thumb" role="img" aria-label="Shopping center listing"></div><h4>Tessaly Market</h4>740 Tessaly Drive<br>Orlando, FL 32801<div class="go">VIEW PROPERTY DETAILS</div></div>
    <div class="card"><div class="thumb" role="img" aria-label="Shopping center listing"></div><h4>Wrenfield Station</h4>1185 Wrenfield Parkway<br>Orlando, FL 32801<div class="go">VIEW PROPERTY DETAILS</div></div>
  </div>
</section>

<section class="news">
  <div class="news-photo" role="img" aria-label="Smiling couple of retail shoppers"></div>
  <div class="abs news-box">
    <h2>Palm Beach Retail in its Fifth Year Recovery</h2>
    <div class="quote">“</div>
    <p>The Palm Beach retail market is in the fifth year of a recovery, with vacancy down more than ten percent from its peak and rents rising as national tenants return to grocery anchored centers.</p>
    <span class="btn">CONTINUE READING</span>
  </div>
</section>

<section class="gallery">
  <div class="gallery-photo" role="img" aria-label="Interior of a shopping mall in soft grey tones"></div>
  <h2>GALLERY</h2>
  <div class="abs arrow" style="left:270px"><svg viewBox="0 0 12 12"><path d="M8 1L3 6l5 5" fill="none" stroke="#fff" stroke-width="2"/></svg></div>
  <div class="abs arrow" style="left:904px"><svg viewBox="0 0 12 12"><path d="M4 1l5 5-5 5" fill="none" stroke="#fff" stroke-width="2"/></svg></div>
  <div class="shots">
    <div class="shot s1" role="img" aria-label="Market storefront"></div>
    <div class="shot s2" role="img" aria-label="Retail center parking lot"></div>
    <div class="shot s3" role="img" aria-label="Shopping center facade"></div>
    <div class="shot s4" role="img" aria-label="Fountain at a plaza in the evening"></div>
    <div class="shot s5" role="img" aria-label="Shopping center at sunset"></div>
    <div class="shot s6" role="img" aria-label="Columned retail arcade"></div>
  </div>
</section>

<footer class="footer">
  <div class="cta"><h2>READY TO TALK ABOUT YOUR NEXT INVESTMENT?</h2><span class="btn">CONTACT US TODAY</span></div>
  <div class="abs fcol" style="left:140px;width:260px">
    <div class="fbrand"><i></i>Maris</div>
    Maris Commercial is a retail real estate firm serving owners and national tenants across Central Florida since 1991.
  </div>
  <div class="abs fcol" style="left:470px"><h5>Quick Links</h5>Our Company<br>Featured Listings<br>Services<br>News<br>Contact Us</div>
  <div class="abs fcol" style="left:630px"><h5>Contact Info</h5>480 Wrenfield Avenue<br>Suite 900<br>Orlando, FL 32801<br>(407) 555-0142<br>hello@mariscommercial.com</div>
  <div class="abs fcol" style="left:810px"><h5>Follow Us</h5><div class="social"><i></i><i></i><i></i><i></i><i></i><i></i></div></div>
  <div class="abs bottom"><span>© 2013 Maris Commercial. All rights reserved.</span><span>Privacy Policy | Terms of Use</span></div>
</footer>

</body>
</html>
```